Modern Informational OBGYN website

Looking for a modern Wordpress website for a general OBGYN practice in Florida with a specialty in High Risk Obstetrics. We had an old Joomla website that crashed and we lost most of the files. It was over 10 years old and needed a refresh anyway.

Our practice serves a multicultural patient population (white, black, Spanish and Indian) and we would like our website to reflect that diversity. Our company colors are sunshine yellow (#ECBF6D) often combined with black, white and steel blue (#7191BE) in the "life" part of our logo (attached) depending on the background. Our tagline is "We're specialist in You!" Overall the site should have a clean modern yet comfortable feel. One that portrays friendliness and competence. At least 6 pages (Home, Obstetrics, Gynecology, News, Patient Education and Resources). Rotating stock pictures or videos are fine for the headers of the pages if the design you're considering calls for it. Interesting and creative use of typography and icons are encouraged.

The home page should have a call to action to schedule an appointment as well as a link to our patient portal. Other than the home and news pages, the other pages should have a similar look and feel. The home page should have sections on "About Us", "Medical Staff" (with pictures and brief bio for 2 male doctors, 2 female midwives and 1 female nurse practitioner), "Services" and "Location". The news page will be a closed blog that will not allow comments or responses. Both the obstetrics and the gynecology pages will have an educational blurb on the respective topics followed by a list of our services for each topic. Would be nice on the obstetrics page to have information and graphics changes that occur during each trimester (but not necessary). The resource page will have sections on at least "Office Forms", Office Policies", "OB Guide" each with multiple downloadable PDF's. Also a section on "Insurance" with a list of all the major insurance plans that we take with links to their company websites. The address, link and map to our hospital and their website can also go on this page. The Patient Education Page can be broken into 3 sections Obstetrics, Gynecology which both will have definition of medical disorders followed by FAQ's and "Helpful Links" which would have links to other website for medical information.

That's all that I can think of right now. The above is to help guide you but I am flexible, if the website design dictates a better flow of information. Looking forward to seeing what you can come up with. Down the road, I will be looking to the winning designer to produce matching brochures, full, half and quarter page media ads to have on hand for the practices further needs.

Target Market(s)

Women looking medical services

Industry/Entity Type

Medical

Coding

Coded - Design and coding required

Number of Pages Required

5+ page

Font styles to use
Sans Serif
Script

Colors

Designer to choose colors to be used in the design.

Requirements
Must have
• None. See projects description for suggestions
Nice to have
• infographics like information on stages of pregnancy on the obstetrics page

```html
<!DOCTYPE html>
<html lang="en">
<head>
<meta charset="utf-8">
<title>Brightday OB/GYN Care</title>
<link href="https://fonts.googleapis.com/css2?family=Lexend:wght@400;500;600&family=Quicksand:wght@400;500;600;700&display=swap" rel="stylesheet">
<style>
:root{
  --sun:#f6b82c;
  --sun-deep:#e9a915;
  --ink:#151515;
  --text:#3a3a3a;
  --muted:#6d6d6d;
  --soft:#f2f4f8;
  --field:#f1f3f7;
  --band:#050505;
  --foot:#3b3b3b;
  --white:#ffffff;
  --wall:#1e5c77;
  --leaf:#4f8a3c;
}
*{box-sizing:border-box;margin:0;padding:0}
html,body{width:1200px;height:4040px;overflow:hidden}
body{font-family:"Quicksand",sans-serif;color:var(--text);background:var(--white);position:relative}
h1,h2,h3,h4,.brand-name{font-family:"Lexend",sans-serif;color:var(--ink);font-weight:500}
.btn{position:absolute;background:var(--sun);color:var(--ink);font-family:"Quicksand",sans-serif;font-weight:700;font-size:13px;display:flex;align-items:center;justify-content:center;border-radius:2px;text-transform:uppercase;letter-spacing:.2px}
.eyebrow{position:absolute;font-size:13px;font-weight:600;color:var(--sun-deep);text-transform:uppercase;display:flex;align-items:center;gap:16px}
.eyebrow::after{content:"";width:70px;height:1px;background:var(--sun)}
.eyebrow.center::before{content:"";width:70px;height:1px;background:var(--sun)}
.photo{position:absolute}

/* header */
.site-header{position:absolute;top:0;left:0;width:1200px;height:110px;background:var(--white)}
.brand{position:absolute;display:flex;align-items:center;gap:10px}
.brand-mark{width:22px;height:22px;border-radius:50%;background:var(--sun)}
.brand-name{font-size:30px;font-weight:600;color:var(--sun);letter-spacing:.5px}
.main-nav{position:absolute;left:350px;top:44px;display:flex;gap:22px;font-size:14px;font-weight:500;color:var(--ink)}
.cta-schedule{left:894px;top:26px;width:220px;height:57px;text-transform:none;font-size:14px}

/* hero */
.hero{position:absolute;top:110px;left:0;width:1200px;height:457px;background:linear-gradient(90deg,#f6f6f7 0%,#f1f2f3 50%,#ebecee 100%)}
.hero-photo{left:600px;top:0;width:600px;height:457px;
  background:
    radial-gradient(ellipse 200px 260px at 28% 55%,rgba(206,210,216,.95) 0%,rgba(206,210,216,0) 100%),
    radial-gradient(ellipse 90px 220px at 86% 48%,rgba(79,138,60,.9) 0%,rgba(79,138,60,0) 100%),
    linear-gradient(180deg,rgba(255,255,255,0) 62%,#e9ecef 74%,#f3f4f5 100%),
    linear-gradient(90deg,#eef0f1 0%,#e4e6e8 38%,#dfe2e5 46%,var(--wall) 47%,#24688a 80%,#2c6f86 100%)}
.hero-photo::before{content:"";position:absolute;left:0;top:0;width:120px;height:100%;background:linear-gradient(90deg,#f1f2f3,rgba(241,242,243,0))}
.hero .eyebrow{left:85px;top:120px;text-transform:none;font-size:14px;font-weight:500}
.hero h1{position:absolute;left:85px;top:148px;font-size:44px}
.hero p{position:absolute;left:85px;top:215px;width:440px;font-size:13.5px;line-height:21px;color:var(--ink);font-weight:500}
.hero .btn{left:86px;top:300px;width:127px;height:42px}

/* about */
.about{position:absolute;top:567px;left:0;width:1200px;height:665px}
.about .main-photo{left:162px;top:101px;width:337px;height:410px;
  background:
    radial-gradient(ellipse 120px 90px at 70% 65%,rgba(236,226,218,.95),rgba(236,226,218,0)),
    radial-gradient(ellipse 110px 140px at 40% 55%,rgba(108,150,200,.8),rgba(108,150,200,0)),
    linear-gradient(180deg,#6d7f8f 0%,#b9c4cd 35%,#e4e8eb 60%,#2a3a52 100%)}
.about .inset{left:85px;top:336px;width:207px;height:229px;background:var(--white);box-shadow:0 6px 24px rgba(0,0,0,.12);padding:11px}
.about .inset div{width:100%;height:100%;background:radial-gradient(ellipse 60% 55% at 50% 45%,#e8c9b8,#efe3da 60%,#f6f3f0)}
.about .eyebrow{left:569px;top:114px}
.about h2{position:absolute;left:569px;top:136px;font-size:40px;line-height:51px;width:560px}
.about .lead{position:absolute;left:569px;top:255px;width:540px;font-size:13px;line-height:21px}
.feature{position:absolute;top:342px;width:260px}
.feature svg{display:block;margin-bottom:14px}
.feature h3{font-size:20px;margin-bottom:12px}
.feature p{font-size:13px;line-height:21px;width:250px}
.about .btn{left:569px;top:506px;width:126px;height:40px}

/* services */
.services{position:absolute;top:1232px;left:0;width:1200px;height:768px;background:var(--soft)}
.services .eyebrow{left:0;width:1200px;justify-content:center;top:97px}
.services h2{position:absolute;top:118px;width:1200px;text-align:center;font-size:40px}
.service-card{position:absolute;top:201px;width:326px;height:467px;background:var(--white);box-shadow:0 4px 18px rgba(0,0,0,.05)}
.service-card .photo{left:0;top:0;width:326px;height:260px}
.service-icon{position:absolute;left:26px;top:192px;width:68px;height:68px;background:var(--sun);display:flex;align-items:center;justify-content:center}
.service-card h3{position:absolute;left:24px;top:290px;font-size:20px}
.service-card p{position:absolute;left:24px;top:326px;width:250px;font-size:13px;line-height:17px}
.service-card a{position:absolute;left:24px;top:414px;font-size:13px;font-weight:600;color:var(--sun-deep);text-decoration:none}

/* staff */
.staff{position:absolute;top:2000px;left:0;width:1200px;height:782px}
.staff .eyebrow{left:85px;top:96px}
.staff h2{position:absolute;left:85px;top:116px;font-size:40px}
.staff .btn{left:988px;top:119px;width:126px;height:43px}
.staff-card{position:absolute;top:196px;width:238px;height:485px;background:var(--white);box-shadow:0 4px 18px rgba(0,0,0,.07);text-align:center}
.staff-card .photo{left:0;top:0;width:238px;height:248px}
.staff-card h3{position:absolute;top:278px;width:100%;font-size:19px}
.staff-card .role{position:absolute;top:308px;width:100%;font-size:13px;color:var(--muted)}
.staff-card p{position:absolute;top:340px;left:24px;width:190px;font-size:13px;line-height:21px}

/* band */
.portal-band{position:absolute;top:2782px;left:0;width:1200px;height:235px;background:radial-gradient(circle at 70% 40%,#1a1a1a,var(--band) 70%)}
.portal-band h2{position:absolute;left:85px;top:67px;font-size:40px;line-height:50px;color:var(--white);font-weight:400}
.portal-band .btn{left:986px;top:96px;width:127px;height:40px;text-transform:none;font-size:14px;font-weight:600}

/* appointment */
.appointment{position:absolute;top:3017px;left:0;width:1200px;height:589px}
.appointment .eyebrow{left:0;width:1200px;justify-content:center;top:96px}
.appointment h2{position:absolute;top:118px;width:1200px;text-align:center;font-size:40px}
.field{position:absolute;background:var(--field);font-size:14px;color:#8a8a8a;padding:0 18px;display:flex;align-items:center;border-radius:2px}
.field.message{align-items:flex-start;padding-top:16px}
.appointment .btn{left:534px;top:447px;width:131px;height:42px}

/* footer */
.site-footer{position:absolute;top:3606px;left:0;width:1200px;height:434px;background:linear-gradient(135deg,#444 0%,var(--foot) 50%,#343434 100%);color:var(--white)}
.site-footer .brand{left:85px;top:72px}
.site-footer .about-text{position:absolute;left:85px;top:176px;width:250px;font-size:13px;line-height:20px}
.socials{position:absolute;left:85px;top:270px;display:flex;gap:16px}
.socials span{width:38px;height:38px;border:1px solid rgba(255,255,255,.25);display:flex;align-items:center;justify-content:center}
.socials span i{width:10px;height:10px;border-radius:50%;background:rgba(255,255,255,.7)}
.foot-col{position:absolute;top:76px}
.foot-col h4{color:var(--white);font-size:21px;font-weight:400;margin-bottom:20px}
.foot-col ul{list-style:none;font-size:13px;line-height:33px}
.foot-col p{font-size:13px;line-height:20px;margin-bottom:14px;width:260px}
.copyright{position:absolute;top:374px;width:1200px;text-align:center;font-size:13px}
</style>
</head>
<body>

<header class="site-header">
  <div class="brand" style="left:85px;top:36px">
    <span class="brand-mark"></span><span class="brand-name">BRIGHTDAY</span>
  </div>
  <nav class="main-nav">
    <span>Home</span><span>Obstetrics</span><span>Gynecology</span><span>News</span><span>Patient Education</span><span>Resources</span>
  </nav>
  <a class="btn cta-schedule">Schedule An Appointment</a>
</header>

<section class="hero">
  <div class="photo hero-photo" role="img" aria-label="Pregnant woman in a grey top beside a tall green plant against a blue wall"></div>
  <div class="eyebrow">Brightday OB/GYN Care</div>
  <h1>We're specialist in You!</h1>
  <p>Lorem Ipsum is simply dummy text of the printing and typesetting industry. Lorem Ipsum has been the industry's standard dummy text ever since Athe 1500s</p>
  <a class="btn">Read More &nbsp;+</a>
</section>

<section class="about">
  <div class="photo main-photo" role="img" aria-label="Doctor performing an ultrasound on a pregnant patient"></div>
  <div class="photo inset"><div role="img" aria-label="Hands forming a heart on a pregnant belly"></div></div>
  <div class="eyebrow">What About Us</div>
  <h2>We Provide general OB/GYN practice in Florida</h2>
  <p class="lead">Lorem Ipsum is simply dummy text of the printing and typesetting industry. Lorem Ipsum has been the industry's standard dummy text ever since the 1500s, when an unknown printer</p>
  <div class="feature" style="left:569px">
    <svg width="34" height="34" viewBox="0 0 34 34" fill="none" stroke="#f6b82c" stroke-width="2"><path d="M17 29S4 21 4 12a7 7 0 0 1 13-3 7 7 0 0 1 13 3c0 9-13 17-13 17z"/><circle cx="17" cy="15" r="4"/></svg>
    <h3>Obstetrics</h3>
    <p>Lorem Ipsum is simply dummy text of the printing</p>
  </div>
  <div class="feature" style="left:847px">
    <svg width="34" height="34" viewBox="0 0 34 34" fill="none" stroke="#f6b82c" stroke-width="2"><rect x="8" y="6" width="18" height="24" rx="2"/><path d="M17 11v8M13 15h8"/></svg>
    <h3>Gynecology</h3>
    <p>Lorem Ipsum is simply dummy text of the printing</p>
  </div>
  <a class="btn">Read More &nbsp;+</a>
</section>

<section class="services">
  <div class="eyebrow center">What We Provide</div>
  <h2>Services We Provided</h2>
  <article class="service-card" style="left:86px">
    <div class="photo" role="img" aria-label="Pregnant woman with a doctor holding a clipboard" style="background:radial-gradient(ellipse 90px 120px at 28% 55%,#e6d2c4,rgba(230,210,196,0)),radial-gradient(ellipse 120px 150px at 72% 45%,#fafafa,rgba(250,250,250,0)),linear-gradient(135deg,#ececea,#f6f6f5 55%,#d5d9dc)"></div>
    <div class="service-icon"><svg width="30" height="30" viewBox="0 0 30 30" fill="none" stroke="#fff" stroke-width="2"><circle cx="15" cy="9" r="5"/><path d="M5 27c0-6 4-10 10-10s10 4 10 10z"/></svg></div>
    <h3>Obstetrics</h3>
    <p>There are many variations of pas of Lorem Ipsum available.There are many variations of pas of Lorem Ipsum available.</p>
    <a>READ MORE &nbsp;+</a>
  </article>
  <article class="service-card" style="left:438px">
    <div class="photo" role="img" aria-label="Doctor showing an anatomical model of the uterus to a patient" style="background:radial-gradient(ellipse 70px 80px at 45% 40%,rgba(90,130,210,.75),rgba(90,130,210,0)),radial-gradient(ellipse 50px 50px at 47% 42%,rgba(230,120,150,.7),rgba(230,120,150,0)),linear-gradient(135deg,#efe9e4,#eef0f4 50%,#dde1e7)"></div>
    <div class="service-icon"><svg width="30" height="30" viewBox="0 0 30 30" fill="none" stroke="#fff" stroke-width="2"><circle cx="15" cy="9" r="5"/><path d="M5 27c0-6 4-10 10-10s10 4 10 10z"/></svg></div>
    <h3>Gynecology</h3>
    <p>There are many variations of pas of Lorem Ipsum available.There are many variations of pas of Lorem Ipsum available.</p>
    <a>READ MORE &nbsp;+</a>
  </article>
  <article class="service-card" style="left:789px">
    <div class="photo" role="img" aria-label="Doctor holding a patient's hands in reassurance" style="background:radial-gradient(ellipse 130px 70px at 50% 62%,#ecc8b0,rgba(236,200,176,0)),radial-gradient(ellipse 140px 120px at 75% 25%,#c9cedd,rgba(201,206,221,0)),linear-gradient(135deg,#dfe3ea,#f1e7df 55%,#eef1f3)"></div>
    <div class="service-icon"><svg width="30" height="30" viewBox="0 0 30 30" fill="none" stroke="#fff" stroke-width="2"><circle cx="15" cy="9" r="5"/><path d="M5 27c0-6 4-10 10-10s10 4 10 10z"/></svg></div>
    <h3>Patient Education</h3>
    <p>There are many variations of pas of Lorem Ipsum available.There are many variations of pas of Lorem Ipsum available.</p>
    <a>READ MORE &nbsp;+</a>
  </article>
</section>

<section class="staff">
  <div class="eyebrow">Our Staff</div>
  <h2>Our Medical Staff</h2>
  <a class="btn">View All &nbsp;+</a>
  <article class="staff-card" style="left:85px">
    <div class="photo" role="img" aria-label="Portrait of a male gynecologist in a white coat" style="background:radial-gradient(ellipse 85px 130px at 50% 72%,#fbfbfb,rgba(251,251,251,0)),radial-gradient(ellipse 40px 45px at 50% 28%,#c9a38a,rgba(201,163,138,0)),linear-gradient(180deg,#eceeef,#dfe2e4)"></div>
    <h3>Dr. Marcus Hale</h3><div class="role">Gynecologist</div>
    <p>Lorem Ipsum is simply dummy text of the printing and typesetting industry. Lorem Ipsum has been the industry's standard dummy text ever</p>
  </article>
  <article class="staff-card" style="left:348px">
    <div class="photo" role="img" aria-label="Portrait of a male gynecologist holding a tablet" style="background:radial-gradient(ellipse 85px 130px at 50% 72%,#f8f9fb,rgba(248,249,251,0)),radial-gradient(ellipse 40px 45px at 50% 28%,#e2b89c,rgba(226,184,156,0)),linear-gradient(180deg,#e9edf2,#d9dfe7)"></div>
    <h3>Dr. Marcus Hale</h3><div class="role">Gynecologist</div>
    <p>Lorem Ipsum is simply dummy text of the printing and typesetting industry. Lorem Ipsum has been the industry's standard dummy text ever</p>
  </article>
  <article class="staff-card" style="left:613px">
    <div class="photo" role="img" aria-label="Portrait of a midwife holding a baby" style="background:radial-gradient(ellipse 90px 120px at 42% 60%,#8a6450,rgba(138,100,80,0)),radial-gradient(ellipse 55px 70px at 66% 55%,#f0d4c0,rgba(240,212,192,0)),linear-gradient(180deg,#f3f3f3,#e1dcd7)"></div>
    <h3>Nia Brooks</h3><div class="role">Midwives</div>
    <p>Lorem Ipsum is simply dummy text of the printing and typesetting industry. Lorem Ipsum has been the industry's standard dummy text ever</p>
  </article>
  <article class="staff-card" style="left:877px">
    <div class="photo" role="img" aria-label="Portrait of a midwife smiling with a baby" style="background:radial-gradient(ellipse 90px 120px at 62% 62%,#5a4a48,rgba(90,74,72,0)),radial-gradient(ellipse 55px 70px at 32% 50%,#f2d6c2,rgba(242,214,194,0)),linear-gradient(180deg,#e2e5e9,#c3c8cf)"></div>
    <h3>Nia Brooks</h3><div class="role">Midwives</div>
    <p>Lorem Ipsum is simply dummy text of the printing and typesetting industry. Lorem Ipsum has been the industry's standard dummy text ever</p>
  </article>
</section>

<section class="portal-band">
  <h2>A general OBGYN practice in Florida<br>with a specialty in High Risk Obstetrics.</h2>
  <a class="btn">Patient Portal</a>
</section>

<section class="appointment">
  <div class="eyebrow center">Appointment</div>
  <h2>Apply for free Checkup</h2>
  <div class="field" style="left:174px;top:197px;width:204px;height:50px">Your Name</div>
  <div class="field" style="left:390px;top:197px;width:204px;height:50px">Gender</div>
  <div class="field" style="left:607px;top:197px;width:203px;height:50px">Your Email</div>
  <div class="field" style="left:822px;top:197px;width:204px;height:50px">Phone No.</div>
  <div class="field message" style="left:174px;top:267px;width:852px;height:143px">Your Message</div>
  <a class="btn">Submit</a>
</section>

<footer class="site-footer">
  <div class="brand">
    <span class="brand-mark"></span><span class="brand-name">BRIGHTDAY</span>
  </div>
  <p class="about-text">It helps designers plan out where the content will sit, the content to be written and approved.</p>
  <div class="socials"><span><i></i></span><span><i></i></span></div>
  <div class="foot-col" style="left:437px">
    <h4>Main Menu</h4>
    <ul><li>Home</li><li>Obstetrics</li><li>Gynecology</li><li>News</li><li>Patient Education</li><li>Resources</li></ul>
  </div>
  <div class="foot-col" style="left:646px">
    <h4>Quick Links</h4>
    <ul><li>FAQ</li><li>Doctors</li><li>Departments</li><li>Events</li><li>Member</li></ul>
  </div>
  <div class="foot-col" style="left:855px">
    <h4>Contact</h4>
    <p style="margin-top:8px">Call : +1800-555-0142</p>
    <p>Email : hello@brightday-care.com</p>
    <p>Location : Lorem ipsum dolor sit amet, consectetur adipiscing elit.</p>
  </div>
  <div class="copyright">Copyright 2022 Brightday OB/GYN Care. All Rights Reserved</div>
</footer>

</body>
</html>
```